street sign 8'x8' AND bee graphic in 10 different poses

Sign graphics should be high visibility . sign should include "2473 Fernhollow" also "Korvana Home Improvements" . also need 10 active bumble bee poses.

```html
<!DOCTYPE html>
<html lang="en">
<head>
<meta charset="utf-8">
<title>2473 Fernhollow – Korvana Home Improvements street sign</title>
<link rel="stylesheet" href="https://fonts.googleapis.com/css2?family=Bebas+Neue&family=Montserrat:wght@400;800&display=swap">
<style>
  :root {
    --navy: #2e3192;
    --orange: #f05a28;
    --green: #2bb673;
    --yellow: #fff200;
    --white: #ffffff;
    --shadow: #8a2a10;
    --timber: #c49a6c;
    --timber-dark: #a97c50;
    --sand: #d6bf7a;
    --bee-gold: #fbb917;
    --bee-amber: #e8951c;
  }
  html, body {
    margin: 0;
    padding: 0;
    width: 1200px;
    height: 1200px;
    overflow: hidden;
    background: var(--navy);
  }
  .sign {
    display: block;
    width: 1200px;
    height: 1200px;
  }
  .street-address {
    font-family: "Bebas Neue", "Arial Narrow", sans-serif;
    fill: var(--white);
  }
  .company-name {
    font-family: "Montserrat", Arial, sans-serif;
    font-weight: 800;
    fill: var(--yellow);
    filter: url(#text-shadow);
  }
  .company-tagline {
    font-family: "Montserrat", Arial, sans-serif;
    font-weight: 400;
    fill: var(--white);
    filter: url(#text-shadow);
  }
  .hill { fill: var(--green); }
  .badge-tile { fill: var(--green); }
  .speech-bubble { fill: var(--orange); }
</style>
</head>
<body>
<svg class="sign" viewBox="0 0 1200 1200" xmlns="http://www.w3.org/2000/svg">
  <defs>
    <filter id="text-shadow" x="-5%" y="-10%" width="115%" height="130%">
      <feDropShadow dx="5" dy="5" stdDeviation="3" flood-color="#8a2a10" flood-opacity="0.85"/>
    </filter>
    <linearGradient id="bee-fill" x1="0" y1="0" x2="0" y2="1">
      <stop offset="0" stop-color="#fbb917"/>
      <stop offset="1" stop-color="#e8951c"/>
    </linearGradient>
    <linearGradient id="frame-fill" x1="0" y1="0" x2="1" y2="0">
      <stop offset="0" stop-color="#c49a6c"/>
      <stop offset="1" stop-color="#a97c50"/>
    </linearGradient>
  </defs>

  <rect class="background" width="1200" height="1200" fill="var(--navy)"/>

  <text class="street-address" x="74" y="219" font-size="210" textLength="1048" lengthAdjust="spacingAndGlyphs">2473 FERNHOLLOW</text>

  <g class="ground">
    <circle class="hill" cx="75" cy="1210" r="150"/>
    <ellipse class="hill" cx="330" cy="1220" rx="200" ry="110"/>
    <ellipse class="hill" cx="890" cy="1200" rx="140" ry="100"/>
    <circle class="hill" cx="1080" cy="1205" r="230"/>
  </g>

  <rect class="house-frame" x="441" y="875" width="586" height="325" fill="url(#frame-fill)" role="img" aria-label="Illustration of a timber house frame under construction with stairs"/>
  <rect class="stairs" x="910" y="1108" width="290" height="92" fill="var(--sand)" role="img" aria-label="Illustration of wooden steps"/>

  <rect class="badge-tile" x="854" y="256" width="289" height="305" rx="50"/>

  <path class="speech-bubble" d="M123 288 H854 V561 H1109 V728 A67 67 0 0 1 1042 795 H917 C860 810 825 850 806 907 C805 850 790 810 737 795 H123 A67 67 0 0 1 56 728 V355 A67 67 0 0 1 123 288 Z"/>

  <text class="company-name" x="134" y="473" font-size="170" textLength="650" lengthAdjust="spacingAndGlyphs">KORVANA</text>
  <text class="company-tagline" x="134" y="593" font-size="114" textLength="328" lengthAdjust="spacingAndGlyphs">HOME</text>
  <text class="company-tagline" x="134" y="713" font-size="114" textLength="888" lengthAdjust="spacingAndGlyphs">IMPROVEMENTS</text>

  <rect class="bee-mascot" x="806" y="290" width="322" height="308" rx="120" fill="url(#bee-fill)" role="img" aria-label="Cartoon bumble bee in a hard hat lying down, peeking over the tile"/>
  <rect class="bee-mascot" x="127" y="737" width="360" height="412" rx="150" fill="url(#bee-fill)" role="img" aria-label="Cartoon bumble bee in a hard hat flying with a hammer"/>
</svg>
</body>
</html>
```